Korvane Works Business cards

We require somebody to design business cards for our new business.

Target Market(s)

Mining, haulage and civil.

Industry/Entity Type

Auto electrician in mining industry

Contact Information for Business Card

ABN, business email address, mobile number.

Colors
00AB8E
00BBA5
67D7C9
C6EFE9
E9F9F6

Requirements
Must have
• Services I offer: Breakdowns, Field Service, A/C Systems, Machine rewires, mine site vehicle fit outs

```html
<!DOCTYPE html>
<html lang="en">
<head>
<meta charset="utf-8">
<title>Korvane Works Business Cards</title>
<link rel="stylesheet" href="https://fonts.googleapis.com/css2?family=Poppins:wght@400;500;700&display=swap">
<style>
  :root {
    --bg: #c9c9c9;
    --card: #1f1f20;
    --teal: #00bba5;
    --teal-light: #67d7c9;
    --teal-pale: #c6efe9;
    --white: #f4f4f4;
    --rule: #2f6b64;
    --silver: #b9bcbd;
  }
  * { box-sizing: border-box; margin: 0; padding: 0; }
  html, body { width: 1200px; height: 802px; overflow: hidden; }
  body {
    background: linear-gradient(180deg, #d3d3d3, #ababab);
    font-family: "Poppins", sans-serif;
    display: flex; align-items: center; justify-content: center; gap: 40px;
  }
  .card {
    position: relative; width: 540px; height: 309px;
    background: var(--card); border-radius: 18px; overflow: hidden;
    box-shadow: 0 18px 40px rgba(0,0,0,.35);
    color: var(--white);
  }
  .brand {
    font-weight: 700; color: var(--teal); letter-spacing: 1px;
    display: flex; align-items: center; gap: 8px; text-transform: uppercase;
  }
  .brand-mark { width: 12px; height: 12px; background: var(--teal); }

  /* front */
  .card-front .brand { position: absolute; top: 40px; right: 36px; font-size: 22px; }
  .card-front .divider {
    position: absolute; left: 36px; right: 36px; top: 150px;
    height: 1px; background: var(--rule);
  }
  .person { position: absolute; left: 36px; top: 98px; }
  .person-name { font-weight: 700; font-size: 22px; color: var(--teal); letter-spacing: 1.5px; line-height: 1.1; }
  .person-role { font-size: 14px; color: var(--white); }
  .contact { position: absolute; left: 36px; top: 166px; list-style: none; font-size: 14px; line-height: 1.6; }
  .contact li { display: flex; align-items: center; gap: 8px; }
  .contact svg { width: 13px; height: 13px; fill: var(--teal); }
  .contact .abn { padding-left: 0; }
  .edge-band {
    position: absolute; left: 0; bottom: 0; width: 100%; height: 16px;
    background: linear-gradient(90deg, var(--teal) 0%, var(--teal-light) 62%, var(--silver) 62.5%, #e4e6e7 80%, var(--silver) 100%);
  }

  /* back */
  .card-back { display: flex; flex-direction: column; align-items: center; padding-top: 78px; }
  .card-back .brand { font-size: 30px; }
  .services-title {
    margin-top: 46px; width: 100%; padding: 0 34px;
    display: flex; align-items: center; gap: 14px;
    font-weight: 700; font-size: 16px; color: var(--teal); white-space: nowrap;
  }
  .services-title::before, .services-title::after { content: ""; flex: 1; height: 1px; background: var(--rule); }
  .services { list-style: none; display: flex; flex-wrap: wrap; justify-content: center; gap: 2px 16px; margin-top: 12px; padding: 0 26px; font-size: 14.5px; }
  .services li::before { content: "•"; color: var(--teal); margin-right: 5px; }
</style>
</head>
<body>
  <section class="card card-front">
    <div class="brand"><span class="brand-mark"></span>Korvane Works</div>
    <div class="person">
      <div class="person-name">SAM HARLOW</div>
      <div class="person-role">Director</div>
    </div>
    <div class="divider"></div>
    <ul class="contact">
      <li class="abn">ABN : 12 345 678 901</li>
      <li><svg viewBox="0 0 24 24"><path d="M6.6 10.8a15 15 0 0 0 6.6 6.6l2.2-2.2c.3-.3.7-.4 1-.2 1.1.4 2.3.6 3.6.6.6 0 1 .4 1 1V20c0 .6-.4 1-1 1A17 17 0 0 1 3 4c0-.6.4-1 1-1h3.5c.6 0 1 .4 1 1 0 1.3.2 2.5.6 3.6.1.3 0 .7-.2 1z"/></svg>0400 118 362</li>
      <li><svg viewBox="0 0 24 24"><path d="M2 5h20v14H2zm2 2v.5l8 5 8-5V7l-8 5z"/></svg>admin@korvaneworks.com.au</li>
    </ul>
    <div class="edge-band"></div>
  </section>

  <section class="card card-back">
    <div class="brand"><span class="brand-mark"></span>Korvane Works</div>
    <div class="services-title">SERVICES I OFFER</div>
    <ul class="services">
      <li>Breakdowns</li>
      <li>Field Service</li>
      <li>A/C Systems</li>
      <li>Machine rewires</li>
      <li>Mine site vehicle fit outs</li>
    </ul>
  </section>
</body>
</html>
```